Business Card Design

I would like a logo created for the top left corner of the card please. I would like a checkerboard in a dark navy with the edges fading out and one random bright orange square.
Updates

I have attached some further notes and a really rough sketch of what I am after.  Thank you. :)

Target Market(s)

Construction, mining, mechanical

Industry/Entity Type

Business

Contact Information for Business Card

KRW Fabrications Pty Ltd, Oscar Plunkett, P. 0413658207, F. 0753917260, E.oscar@krwfabrications.com.au, PO Box 87 WONGARA Q 4571, ABN 52983470611

Font styles to use
Sans Serif

Requirements
Must have
• Really Dark Navy
Really bright Orange

```html
<!DOCTYPE html>
<html lang="en">
<head>
<meta charset="utf-8">
<title>KRW Fabrications Pty Ltd – Business Card</title>
<link rel="stylesheet" href="https://fonts.googleapis.com/css2?family=Arimo:wght@400;700&display=swap">
<style>
  :root {
    --page: #fefefe;
    --navy: #005a92;
    --navy-light: #4f8cb8;
    --orange: #e85c00;
    --grey-top: #bfbfbf;
    --grey-bottom: #fbfbfb;
    --charcoal: #2a2a2a;
    --ink-light: #dbe8f2;
    --white: #ffffff;
  }
  html, body {
    margin: 0;
    width: 1200px;
    height: 1000px;
    overflow: hidden;
    background: var(--page);
    font-family: "Arimo", Arial, sans-serif;
  }
  .card {
    position: absolute;
    left: 153px;
    top: 255px;
    width: 898px;
    height: 461px;
    box-shadow: 0 0 3px rgba(0,0,0,0.45);
    overflow: hidden;
  }
  .card-front {
    position: absolute;
    left: 0; top: 0;
    width: 898px; height: 272px;
    background: linear-gradient(to bottom, var(--grey-top), var(--grey-bottom));
  }
  .wave-art {
    position: absolute;
    left: 0; top: 0;
    width: 898px; height: 272px;
    background: linear-gradient(200deg, rgba(42,42,42,0) 35%, rgba(42,42,42,0.28) 70%, rgba(42,42,42,0.5) 100%);
  }
  .brand {
    position: absolute;
    right: 24px;
    top: 130px;
    display: flex;
    align-items: center;
    gap: 10px;
  }
  .brand-square {
    width: 22px; height: 22px;
    background: var(--orange);
  }
  .brand-name {
    color: var(--orange);
    font-weight: 700;
    font-size: 32px;
    letter-spacing: -0.3px;
  }
  .accent-band {
    position: absolute;
    left: 0; top: 272px;
    width: 898px; height: 9px;
    background: var(--orange);
  }
  .card-details {
    position: absolute;
    left: 0; top: 281px;
    width: 898px; height: 180px;
    background: var(--navy);
    color: var(--white);
  }
  .company {
    position: absolute;
    left: 13px; top: 36px;
    margin: 0;
    font-size: 21px;
    font-weight: 700;
    letter-spacing: 0.6px;
  }
  .summary {
    position: absolute;
    left: 13px; top: 69px;
    margin: 0;
    font-size: 15px;
    color: var(--ink-light);
    white-space: nowrap;
  }
  .contact {
    position: absolute;
    top: 96px;
    margin: 0;
    font-size: 16px;
    line-height: 24px;
  }
  .contact-left { left: 13px; }
  .contact-right { left: 211px; }
  .dot-art {
    position: absolute;
    left: 608px; top: 2px;
    width: 256px; height: 178px;
    background: radial-gradient(ellipse at 50% 45%, rgba(219,232,242,0.55), rgba(79,140,184,0.25) 55%, rgba(0,90,146,0) 80%);
  }
</style>
</head>
<body>
  <div class="card">
    <div class="card-front">
      <div class="wave-art" role="img" aria-label="Dark halftone dot wave pattern sweeping across the card"></div>
      <div class="brand">
        <span class="brand-square"></span>
        <span class="brand-name">KRW Fabrications Pty Ltd</span>
      </div>
    </div>
    <div class="accent-band"></div>
    <div class="card-details">
      <h1 class="company">KRW Fabrications Pty Ltd</h1>
      <p class="summary">KRW Fabrications Pty Ltd Oscar Plunkett 0413 658 207 PO Box 87 WONGARA Q 4571</p>
      <p class="contact contact-left">Phone: 0413 658 207<br>Fax: 07 5391 7260</p>
      <p class="contact contact-right">Email:&nbsp; oscar@krwfabrications.com.au<br>ABN 52 983 470 611</p>
      <div class="dot-art" role="img" aria-label="Light blue halftone dot pattern decoration"></div>
    </div>
  </div>
</body>
</html>
```